Brisvane Partners Web Design

Dear all
I need a web design for a financial services site. We are a broker who deals with many different financial institutions and require a clean, simple and instantly impressive site based on the colour scheme that Mockwell created for us. A landing page (www.brisvn.mx) gives an idea of the logo and clour scheme but we are looking at either a one page site with rollover text boxes or a 3 or 4 page site depending on the preference of the designer and the best user experience. The site“s purpose is to give confidence that the company exists rather than impart pages of information although we would like this to be a site that can expand over time as the company grows. For now the requirement is for a clear set of possibly changing images at the centre of a white screen that relate to finance in general nad the benefits of wealth creation as well as sectios either along the top or bottom - Our Company, Our Approach, Our services, Our clients, Contact (user to fill in contact box to be sent to info@brisvn.mx. The text for each of these boxes I assume can be added by the coding team here, it the overall look and feel that I am looking for from Mockwell - deadline can be extended if necessary but I was hoping to wrap this all up in October

Target Market(s)

Succesful individuals looking to maximise returns on their investment via world class financial institutions and supported throughout by qualified independent financial advisors

Industry/Entity Type

Finance

Requirements
Must have
• Logo and color scheme of the logo design Mockwell sent - I have all these sourcefiles, pantone and fonts

```html
<!DOCTYPE html>
<html lang="en">
<head>
<meta charset="utf-8">
<title>Brisvane Partners</title>
<link rel="stylesheet" href="https://fonts.googleapis.com/css2?family=Arimo:wght@400;700&family=Roboto+Condensed:wght@400;700&display=swap">
<style>
:root{
  --navy:#1e3a63;
  --navy-deep:#172f52;
  --orange:#f0a030;
  --cream:#f4f9ea;
  --ink:#555b66;
  --heading:#2c4a7c;
  --white:#ffffff;
  --line:#d6dbc8;
}
*{box-sizing:border-box;margin:0;padding:0}
html,body{width:1200px;height:2174px;overflow:hidden}
body{position:relative;background:var(--white);font-family:"Arimo",Arial,sans-serif;color:var(--ink)}
.abs{position:absolute}
ul{list-style:none}

/* top bar */
.topbar{left:0;top:0;width:1200px;height:52px;background:var(--navy);color:var(--white);font-size:11px}
.utility{left:89px;top:19px;display:flex;gap:10px}
.mainnav{right:46px;top:20px;display:flex;gap:30px;font-size:11px;text-transform:uppercase}
.mainnav .active{color:var(--orange)}

/* hero */
.hero{left:0;top:52px;width:1200px;height:550px;background:linear-gradient(100deg,#e6ecf3 0%,#c9d5e3 30%,#8ea3bd 55%,#2d4a73 75%,#dfe6ee 100%)}
.brand{left:83px;top:100px;display:flex;align-items:center;gap:14px}
.brand-mark{width:40px;height:40px;background:var(--orange);border-radius:50%}
.brand-name{font-size:30px;color:var(--navy);letter-spacing:3px;font-weight:400}
.support{left:89px;top:307px;font-size:21px;color:var(--navy)}
.promo{left:89px;top:381px;width:452px;height:132px;background:var(--orange);color:var(--white);padding:30px 20px 0 42px}
.promo-title{font-size:21px;line-height:32px;width:395px}
.promo-more{position:absolute;right:44px;top:78px;font-size:11px;color:var(--navy-deep)}
.arrow{top:533px;width:54px;height:49px;display:flex;align-items:center;justify-content:center}
.arrow.prev{left:89px;background:var(--orange)}
.arrow.next{left:152px;background:var(--navy)}

/* about */
.section-title{width:1200px;left:0;text-align:center;font-family:"Roboto Condensed",Arial,sans-serif;font-weight:400;font-size:26px;color:var(--heading)}
.section-title em{font-style:normal;color:var(--orange)}
.about-text{left:105px;top:760px;width:992px;text-align:center;font-size:13px;line-height:23px;color:#6a6f77}

/* services */
.service{width:180px;text-align:center;top:1017px}
.service-icon{width:122px;height:122px;border-radius:50%;background:var(--navy);margin:0 auto;display:flex;align-items:center;justify-content:center}
.service-icon.light{background:#eef6de}
.service-label{margin-top:20px;font-size:13px;font-weight:700;color:var(--heading)}

/* news band */
.news-band{left:0;top:1237px;width:1200px;height:569px;background:var(--cream)}
.news-item{left:87px;width:470px;height:90px}
.date{position:absolute;left:0;top:0;width:93px;height:80px;background:var(--navy);text-align:center;color:var(--white)}
.date b{display:block;font-family:"Roboto Condensed",Arial,sans-serif;color:var(--orange);font-size:21px;padding-top:17px}
.date span{font-size:14px}
.news-head{position:absolute;left:120px;top:0;font-size:13px;font-weight:700;color:var(--navy)}
.news-body{position:absolute;left:120px;top:38px;width:340px;font-size:13px;line-height:22px;color:#6a6f77}
.view-all{left:207px;top:1744px;font-size:13px;font-weight:700;color:var(--navy)}
.divider{left:570px;top:1356px;height:420px;border-left:1px dashed #c7ccbc}

.media{left:620px;top:1357px;width:489px;height:343px;border:1px solid var(--line);background:#fbfdf6}
.tabs{display:flex;height:39px}
.tab{flex:1;background:#dde2d6;color:var(--navy);font-size:13px;display:flex;align-items:center;justify-content:center}
.tab.active{background:var(--navy);color:var(--white);position:relative}
.tab.active::after{content:"";position:absolute;bottom:-7px;left:50%;margin-left:-7px;border:7px solid transparent;border-bottom:0;border-top-color:var(--navy)}
.video{position:absolute;left:20px;top:60px;width:448px;height:265px;background:linear-gradient(135deg,#3a3c40,#6d6358 50%,#2a2b2e);display:flex;align-items:center;justify-content:center}
.play{width:36px;height:32px;background:#d8262a;display:flex;align-items:center;justify-content:center;border-radius:4px}

/* footer */
.footer{left:0;top:1806px;width:1200px;height:320px;background:var(--navy);color:var(--white)}
.footer-col{top:55px}
.footer-col h3{font-family:"Roboto Condensed",Arial,sans-serif;font-weight:400;font-size:17px;color:var(--orange);margin-bottom:22px}
.footer-col li{font-size:13px;line-height:23.3px}
.contact-lines{font-size:13px;line-height:20px}
.mail-title{font-family:"Roboto Condensed",Arial,sans-serif;font-size:17px;color:var(--orange);margin:14px 0 8px}
.bottombar{left:0;top:2126px;width:1200px;height:48px;background:var(--navy-deep);color:var(--white);font-size:12px}
.copyright{left:89px;top:17px}
.follow{right:50px;top:8px;display:flex;align-items:center;gap:6px}
.follow span{margin-right:6px;font-size:12px}
.social{width:34px;height:34px;border-radius:6px;background:#4c7fc8}
</style>
</head>
<body>

<header class="abs topbar">
  <div class="abs utility"><span>Help Desk</span><span>|</span><span>Sign in</span><span>|</span><span>Register</span></div>
  <nav class="abs mainnav">
    <span class="active">Home</span><span>Invetment</span><span>About us</span><span>Services</span><span>Onlie calculator</span><span>News &amp; Blog</span><span>Contact us</span>
  </nav>
</header>

<section class="abs hero" role="img" aria-label="Photo of business advisors in suits reviewing financial documents at a desk"></section>
<div class="abs brand"><span class="brand-mark"></span><span class="brand-name">Brisvane Partners</span></div>
<div class="abs support">Quick Support : 000-0000-0000</div>
<div class="abs promo">
  <p class="promo-title">Creating your success through Financial Planning</p>
  <span class="promo-more">Learn more &gt;&gt;</span>
</div>
<div class="abs arrow prev"><svg width="14" height="24" viewBox="0 0 14 24"><path d="M12 2 2 12l10 10" fill="none" stroke="#fff" stroke-width="2"/></svg></div>
<div class="abs arrow next"><svg width="14" height="24" viewBox="0 0 14 24"><path d="M2 2l10 10L2 22" fill="none" stroke="#fff" stroke-width="2"/></svg></div>

<h2 class="abs section-title" style="top:694px">Something about <em>Brisvane Financial Group</em></h2>
<p class="abs about-text">Lorem Ipsum is simply dummy text of the printing and typesetting industry. Lorem Ipsum has been the industry's standard dummy text ever since the 1500s, when an unknown printer took a galley of type and scrambled it to make a type specimen book. It has survived not only five centuries, but also the leap into electronic typesetting, remaining essentially unchanged. It was popularised in the 1960s with the release of Letterform sheets containing Lorem Ipsum passages, and more recently with desktop publishing software like Pagecraft Publisher including versions of Lorem Ipsum.</p>

<h2 class="abs section-title" style="top:944px">Services We Are Providing</h2>

<div class="abs service" style="left:95px">
  <div class="service-icon light"><svg width="52" height="44" viewBox="0 0 52 44"><rect x="2" y="10" width="48" height="32" rx="3" fill="#1e3a63"/><rect x="18" y="3" width="16" height="9" rx="2" fill="none" stroke="#1e3a63" stroke-width="3"/><rect x="23" y="20" width="6" height="5" fill="#eef6de"/></svg></div>
  <p class="service-label">Investment</p>
</div>
<div class="abs service" style="left:304px">
  <div class="service-icon"><svg width="48" height="48" viewBox="0 0 48 48"><path d="M4 22a20 18 0 0 1 40 0z" fill="#fff"/><path d="M24 22v16a4 4 0 0 1-8 0" fill="none" stroke="#fff" stroke-width="3"/></svg></div>
  <p class="service-label">Life Insurance</p>
</div>
<div class="abs service" style="left:512px">
  <div class="service-icon"><svg width="56" height="46" viewBox="0 0 56 46"><circle cx="16" cy="26" r="14" fill="#fff"/><text x="16" y="32" text-anchor="middle" font-family="Arimo,Arial,sans-serif" font-weight="700" font-size="17" fill="#1e3a63">$</text><g fill="#fff"><rect x="32" y="6" width="22" height="5"/><rect x="32" y="14" width="22" height="5"/><rect x="32" y="22" width="22" height="5"/><rect x="32" y="30" width="22" height="5"/><rect x="32" y="38" width="22" height="5"/></g></svg></div>
  <p class="service-label">Income protection</p>
</div>
<div class="abs service" style="left:719px">
  <div class="service-icon"><svg width="52" height="46" viewBox="0 0 52 46"><path d="M26 3 2 24h7v20h34V24h7z" fill="#fff"/><rect x="21" y="30" width="10" height="14" fill="#1e3a63"/></svg></div>
  <p class="service-label">Mortgage protection</p>
</div>
<div class="abs service" style="left:925px">
  <div class="service-icon"><svg width="50" height="50" viewBox="0 0 50 50"><rect x="4" y="10" width="34" height="34" fill="none" stroke="#fff" stroke-width="4"/><path d="M18 32l3-9 20-20 6 6-20 20z" fill="#fff"/></svg></div>
  <p class="service-label">Pensions</p>
</div>

<section class="abs news-band"></section>
<h2 class="abs section-title" style="top:1281px">Latest News and Testimonials</h2>

<article class="abs news-item" style="top:1356px">
  <div class="date"><b>OCT 22</b><span>2013</span></div>
  <h3 class="news-head">News Headline Goes Here</h3>
  <p class="news-body">Lorem Ipsum is simply dummy text of the printing and typesetting industry. Lorem Ipsum has</p>
</article>
<article class="abs news-item" style="top:1489px">
  <div class="date"><b>OCT 22</b><span>2013</span></div>
  <h3 class="news-head">News Headline Goes Here</h3>
  <p class="news-body">Lorem Ipsum is simply dummy text of the printing and typesetting industry. Lorem Ipsum has</p>
</article>
<article class="abs news-item" style="top:1622px">
  <div class="date"><b>OCT 22</b><span>2013</span></div>
  <h3 class="news-head">News Headline Goes Here</h3>
  <p class="news-body">Lorem Ipsum is simply dummy text of the printing and typesetting industry. Lorem Ipsum has</p>
</article>
<div class="abs view-all">View All &nbsp;&gt;&gt;</div>
<div class="abs divider"></div>

<div class="abs media">
  <div class="tabs"><span class="tab">Online Calucator</span><span class="tab active">Watch video</span><span class="tab">Testimonials</span></div>
  <div class="video" role="img" aria-label="Video still of a client testimonial">
    <div class="play"><svg width="12" height="14" viewBox="0 0 12 14"><path d="M0 0l12 7-12 7z" fill="#fff"/></svg></div>
  </div>
</div>

<footer class="abs footer">
  <div class="abs footer-col" style="left:87px"><h3>Quick Links</h3>
    <ul><li>Home</li><li>About us</li><li>Services</li><li>Technology</li><li>News and Blog</li><li>Contact us</li><li>Privacy lokicy</li><li>Terms of Use</li></ul></div>
  <div class="abs footer-col" style="left:350px"><h3>How can we help</h3>
    <ul><li>Buying a home</li><li>Refinancing</li><li>Investing</li><li>First Home Buyers</li><li>Commercial Finance</li><li>Brisvane Property</li></ul></div>
  <div class="abs footer-col" style="left:620px"><h3>Online calculators</h3>
    <ul><li>Loan Options Calculator</li><li>Split Loan Calculator</li><li>Extra Repayment Calculator</li><li>Borrowing Power Calculator</li><li>Stamp Duty Calculator</li><li>Budget Planner</li></ul></div>
  <div class="abs footer-col" style="left:887px"><h3>Contact us</h3>
    <div class="contact-lines">PH. &nbsp;NO : 000-0000-000<br>Email &nbsp;&nbsp;: info@brisvn.mx<br>Fax &nbsp;&nbsp;&nbsp;&nbsp;&nbsp;: info@brisvn.mx</div>
    <div class="mail-title">Mailing Address :</div>
    <div class="contact-lines">Company Mailling Address<br>Goes Here :</div></div>
</footer>

<div class="abs bottombar">
  <div class="abs copyright">Copyright © 2013 brisvn.mx</div>
  <div class="abs follow"><span>FOLLOW US :</span><i class="social"></i><i class="social"></i><i class="social"></i></div>
</div>

</body>
</html>
```